M&A Advisory firm needs elegant and powerful letterhead

We need a powerful but elegant letterhead to engage with the international financial industry.

Target Market(s)

New York and International Financial Industry

Industry/Entity Type

Finance

Font styles to use
Other font styles liked:
• Poppins

Requirements
Must have
• 482 W 71st Street 14th Floor New York, NY 10157 O: +1 (212) 555 0147 F: +1 (212) 555 0182

```html
<!DOCTYPE html>
<html lang="en">
<head>
<meta charset="utf-8">
<title>Halden Letterhead</title>
<link href="https://fonts.googleapis.com/css2?family=Montserrat:wght@300;600&family=Open+Sans:wght@400;600&family=Questrial&family=Poppins:wght@400&display=swap" rel="stylesheet">
<style>
  :root {
    --brand-blue: #0b5394;
    --ink-grey: #8e8e8e;
    --name-grey: #9b9b9b;
    --address-grey: #555b63;
    --paper: #ffffff;
    --signature-tone: #eef0f4;
  }
  * { margin: 0; padding: 0; box-sizing: border-box; }
  html, body { width: 1068px; height: 1200px; overflow: hidden; background: var(--paper); }
  .letterhead { position: relative; width: 1068px; height: 1200px; background: var(--paper); overflow: hidden; }

  .brand { position: absolute; left: 48px; top: 78px; display: flex; align-items: center; gap: 14px; }
  .brand-dot { width: 48px; height: 48px; border-radius: 50%; background: var(--brand-blue); }
  .brand-name { font-family: 'Poppins', sans-serif; font-weight: 400; font-size: 56px; letter-spacing: 1px; color: var(--brand-blue); line-height: 1; }

  .office-address { position: absolute; right: 64px; top: 100px; display: flex; gap: 8px; font-family: 'Open Sans', sans-serif; font-size: 17px; line-height: 22px; color: var(--address-grey); }
  .pin { width: 18px; height: 18px; flex: none; margin-top: 2px; }

  .sender { position: absolute; left: 76px; top: 296px; font-family: 'Montserrat', sans-serif; color: var(--ink-grey); }
  .sender-name { font-weight: 600; font-size: 27px; color: var(--name-grey); letter-spacing: 0.5px; margin-bottom: 10px; }
  .sender-line { font-weight: 300; font-size: 15.5px; line-height: 20px; margin-bottom: 7px; }

  .letter-date { position: absolute; right: 71px; top: 402px; font-family: 'Open Sans', sans-serif; font-weight: 600; font-size: 17px; color: var(--name-grey); }

  .letter-body { position: absolute; left: 71px; width: 926px; top: 452px; font-family: 'Questrial', sans-serif; font-size: 15.5px; line-height: 18.8px; color: var(--ink-grey); text-align: justify; }
  .letter-body p { margin-bottom: 18px; }
  .letter-body p.tight { margin-bottom: 0; }
  .letter-body p.gap { margin-top: 36px; }

  .signatory-title { position: absolute; left: 70px; top: 836px; font-family: 'Questrial', sans-serif; font-size: 23px; color: var(--ink-grey); }
  .signature { position: absolute; left: 82px; top: 880px; width: 140px; height: 96px; background: var(--signature-tone); border-radius: 4px; }

  .contact-band { position: absolute; left: 0; top: 1135px; width: 712px; height: 37px; }
  .contact-band svg.band { position: absolute; inset: 0; }
  .contact-item { position: absolute; top: 7px; display: flex; align-items: center; gap: 8px; font-family: 'Open Sans', sans-serif; font-size: 17px; color: #fff; }
  .contact-item svg { width: 20px; height: 20px; }
  .contact-phone { left: 72px; }
  .contact-fax { left: 330px; }
</style>
</head>
<body>
<main class="letterhead">
  <header>
    <div class="brand">
      <span class="brand-dot"></span>
      <span class="brand-name">HALDEN</span>
    </div>
    <div class="office-address">
      <svg class="pin" viewBox="0 0 18 18"><rect width="18" height="18" rx="2" fill="var(--brand-blue)"/><path d="M9 3.5a4 4 0 0 0-4 4c0 3 4 7 4 7s4-4 4-7a4 4 0 0 0-4-4zm0 5.6a1.6 1.6 0 1 1 0-3.2 1.6 1.6 0 0 1 0 3.2z" fill="#fff"/></svg>
      <div>482 W 71st Street 14th Floor<br>New York, NY 10157</div>
    </div>
  </header>

  <section class="sender">
    <div class="sender-name">CLARA BENTON</div>
    <div class="sender-line">0198-274-365</div>
    <div class="sender-line">c.benton@haldenadvisory.com</div>
    <div class="sender-line">5870 Ridgeview Ave. Suite<br>310 Dallas, TX 75201</div>
  </section>

  <div class="letter-date">12 December, 2023</div>

  <article class="letter-body">
    <p>Lorem ipsum dolor sit amet, consectetuer adipiscing elit, sed diam nonummy nibh euismod tincidunt ut laoreet dolore magna aliquam erat volutpat. Ut wisi enim ad minim veniam, quis nostrud exerci tation ullamcorper suscipit lobortis nisl ut aliquip ex ea commodo consequat. Duis autem vel eum iriure dolor in hendrerit in vulputate velit esse molestie consequat, vel illum dolore eu feugiat nulla facilisis at vero eros et accumsan et iusto odio dignissim qui blandit praesent luptatum zzril delenit augue duis dolore te feugait nulla facilisi.</p>
    <p class="tight">Lorem ipsum dolor sit amet, cons ectetuer adipiscing elit, sed diam nonummy nibh euismod tincidunt ut laoreet dolore magna aliquam erat volutpat. Ut wisi enim ad minim veniam, quis nostrud exerci tation ullamcorper suscipit lobortis nisl ut aliquip ex ea commodo consequat.</p>
    <p>Lorem ipsum dolor sit amet, consectetuer adipiscing elit, sed diam nonummy nibh euismod tincidunt ut laoreet dolore magna aliquam erat</p>
    <p class="gap">Lorem ipsum dolor sit amet, cons ectetuer adipiscing elit, sed diam nonummy nibh euismod tincidunt ut laoreet dolore magna aliquam erat volutpat. Ut wisi enim ad minim veniam, quis nostrud exerci tation ullamcorper suscipit lobortis nisl ut aliquip ex ea commodo consequat. Lorem ipsum dolor sit zamet, consectetuer adipiscing elit, sed diam nonummy nibh euismod tincidunt.</p>
  </article>

  <div class="signatory-title">Managing Director</div>
  <div class="signature" role="img" aria-label="Handwritten signature of the managing director"></div>

  <footer class="contact-band">
    <svg class="band" viewBox="0 0 712 37" preserveAspectRatio="none"><polygon points="0,0 672,0 712,37 0,37" fill="var(--brand-blue)"/></svg>
    <div class="contact-item contact-phone">
      <svg viewBox="0 0 20 20"><rect width="20" height="20" rx="2" fill="#fff"/><path d="M6.2 4.2l2 2.3-1.2 1.6c.9 1.9 2.3 3.3 4.2 4.2l1.6-1.2 2.3 2-1.2 2.1c-4.7-.4-8.6-4.3-9-9z" fill="var(--brand-blue)"/></svg>
      <span>+1 (212) 555 0147</span>
    </div>
    <div class="contact-item contact-fax">
      <svg viewBox="0 0 20 20"><rect width="20" height="20" rx="2" fill="#fff"/><rect x="6" y="4" width="8" height="4" fill="none" stroke="var(--brand-blue)" stroke-width="1.3"/><rect x="3.5" y="8" width="13" height="6" rx="1" fill="var(--brand-blue)"/><rect x="6" y="12" width="8" height="4.5" fill="#fff" stroke="var(--brand-blue)" stroke-width="1.3"/></svg>
      <span>+1 (212) 555 0182</span>
    </div>
  </footer>
</main>
</body>
</html>
```